Website - Tides Of Bloom

We are catalysts of change in people's lives.
We work with individuals and professionals to bring about instant substantial & transforming change in their lives.
We provide one-on-one lifestyle coaching by an experienced practitioner.
Our existing website is www.tidesofbloom.biz & this site contains our the basis for the content of our desired new project, so please examine this carefully.
We require a professional and captivating website that will instantly impress, engage invite our readers to click & invest their lives.
Our services do not come cheap, but are second to none.
Our website must be contemporary whilst reflecting indisputable class & ultra-confidence in the success of our work.
Target Market(s)
Those who seek to want to change in their lives. Those aged primarily between 30 and 50 years of age, male or female.
Industry/Entity Type
Work
Look and feel

```html
<!DOCTYPE html>
<html lang="en">
<head>
<meta charset="utf-8">
<title>Tides Of Bloom</title>
<link href="https://fonts.googleapis.com/css2?family=Roboto+Condensed:wght@400;700&display=swap" rel="stylesheet">
<style>
:root{
  --black:#000;
  --ink:#111;
  --white:#fff;
  --grey:#8e8e8e;
  --card-grey:#9a9a9a;
  --blue:#5ec6d9;
  --orange:#f05a28;
  --amber:#f7931e;
  --green:#8dc63f;
  --footer:#2e2e2e;
}
*{margin:0;padding:0;box-sizing:border-box}
html,body{width:1200px;height:2251px;overflow:hidden;background:var(--black)}
body{font-family:"Roboto Condensed",Arial,sans-serif;color:var(--white);position:relative}
.abs{position:absolute}
/* header */
.site-header{left:0;top:0;width:1200px;height:113px;background:var(--black)}
.brand{left:34px;top:18px;display:flex;align-items:center;gap:12px}
.brand-dot{width:50px;height:50px;border-radius:50%;background:var(--amber)}
.brand-name{font-size:27px;font-weight:700;line-height:1;color:var(--white);width:120px}
.header-phone{right:58px;top:10px;display:flex;align-items:center;gap:12px;font-size:25px;font-weight:700}
.main-nav{right:46px;top:72px;display:flex;gap:58px;font-size:20px}
.main-nav a{color:var(--white);text-decoration:none}
.main-nav a.active{color:var(--orange)}
/* hero */
.hero{left:0;top:113px;width:1200px;height:472px;background:linear-gradient(180deg,#cfc1a6 0%,#b9a283 35%,#8a6b48 55%,#6a5a4a 75%,#4b443e 100%)}
.hero-panel{left:608px;top:338px;width:592px;height:209px;background:rgba(40,36,32,.72)}
.hero-line1{left:650px;top:366px;font-size:31px;font-weight:700;color:var(--blue);white-space:nowrap}
.hero-line1 em{font-style:normal;color:var(--amber)}
.hero-line2{left:763px;top:402px;font-size:31px;font-weight:700;color:var(--green)}
.cta{left:727px;top:461px;width:369px;height:57px;border-radius:12px;background:var(--orange);font-size:35px;font-weight:700;display:flex;align-items:center;justify-content:center}
/* services */
.services{left:0;top:585px;width:1200px;height:462px;background:#0c0c0c;border-bottom:2px solid #ddd}
.card{top:27px;width:360px;height:406px;background:var(--white);border-radius:12px;overflow:hidden;color:var(--ink)}
.card-head{height:108px;background:var(--card-grey);border-bottom:8px solid var(--blue);position:relative}
.card-head::after{content:"";position:absolute;left:120px;bottom:-8px;width:120px;height:8px;background:var(--amber)}
.card-head::before{content:"";position:absolute;right:0;bottom:-8px;width:120px;height:8px;background:var(--green);z-index:1}
.card-icon{position:absolute;left:128px;top:2px;width:104px;height:104px}
.card-title{text-align:center;font-size:31px;line-height:36px;font-weight:700;margin-top:10px}
.card-text{padding:4px 26px 0 34px;font-size:16.5px;line-height:22.5px;text-transform:uppercase}
/* success */
.section-title{font-size:30px;font-weight:700;color:var(--blue);white-space:nowrap}
.section-title .o{color:var(--amber)}
.section-title .g{color:var(--green)}
.success-list{left:32px;top:1122px;list-style:none;font-size:17.5px;text-transform:uppercase}
.success-list li{height:31.6px;display:flex;align-items:center;gap:10px}
.success-list svg{flex:none}
.laptop{left:722px;top:1144px;width:440px;height:236px}
.rule{left:0;width:1200px;height:2px;background:#ddd}
/* featured */
.feature{top:1511px;width:220px;height:220px;border-radius:50%;border:4px solid var(--white)}
.slide-arrow{top:1601px;width:40px;height:40px}
/* team */
.team{left:0;top:1774px;width:1200px;height:293px;background:var(--blue)}
.avatar{top:1788px;width:104px;height:104px;border-radius:50%;border:4px solid var(--white);background:linear-gradient(180deg,#9a9a9a,#4d4d4d)}
.member-name{top:1818px;font-size:15px;font-weight:700;color:var(--orange);text-transform:uppercase}
.member-name span{color:var(--ink)}
.member-text{top:1898px;width:450px;font-size:13.5px;line-height:29px;text-align:center;color:var(--ink);text-transform:uppercase}
.read-more{left:507px;top:2001px;width:207px;height:41px;background:var(--orange);display:flex;align-items:center;justify-content:center;font-size:21px;font-weight:700}
/* footer */
.site-footer{left:0;top:2067px;width:1200px;height:184px;background:var(--footer)}
.footer-phone{left:44px;top:2086px;display:flex;align-items:center;gap:18px;font-size:38px;font-weight:700}
.follow{left:812px;top:2082px;display:flex;align-items:center;gap:14px;font-size:37px;font-weight:700}
.social{width:68px;height:68px;border-radius:50%;background:var(--white)}
.footer-nav{left:132px;top:2160px;display:flex;gap:42px;font-size:17px}
.copyright{left:222px;top:2198px;font-size:13px}
.footer-brand{left:976px;top:2170px;display:flex;align-items:center;gap:10px}
.footer-brand .brand-dot{width:44px;height:44px}
.footer-brand .brand-name{font-size:22px;width:100px}
</style>
</head>
<body>

<header class="site-header abs">
  <div class="brand abs"><span class="brand-dot"></span><span class="brand-name">Tides Of Bloom</span></div>
  <div class="header-phone abs">
    <svg width="40" height="40" viewBox="0 0 40 40"><circle cx="20" cy="20" r="18" fill="none" stroke="#fff" stroke-width="2.5"/><path d="M13 11c2-1 3 0 4 3l-1 3c1 3 3 5 6 6l3-1c3 1 4 2 3 4-2 3-5 3-9 0s-7-7-8-10 0-4 2-5z" fill="#fff"/></svg>
    CALL US: +61 02 5550 1234
  </div>
  <nav class="main-nav abs"><a class="active">HOME</a><a>BUSINESS</a><a>INDIVIDUAL</a><a>CONTACT</a></nav>
</header>

<section class="hero abs" role="img" aria-label="Photo of a runner silhouetted on a beach at sunset"></section>
<div class="hero-panel abs"></div>
<p class="hero-line1 abs">INSTANTLY IMPRESS, <em>ENGAGE READERS</em></p>
<p class="hero-line2 abs">INVEST THEIR LIVES....</p>
<div class="cta abs">GET STARTED NOW</div>

<section class="services abs">
  <article class="card abs" style="left:36px">
    <div class="card-head"><svg class="card-icon" viewBox="0 0 104 104"><circle cx="52" cy="52" r="46" fill="#fff" stroke="#333" stroke-width="6"/><path d="M30 56h36l-10-12M66 56l-10 12" fill="none" stroke="#333" stroke-width="8" stroke-linecap="round" stroke-linejoin="round"/></svg></div>
    <h2 class="card-title">LIFE SKILLS</h2>
    <p class="card-text">Lorem ipsum is simply dummy text of the printing and typesetting industry. Lorem ipsum has been the industry's standard dummy text ever since the 1500s, when an unknown printer took a galley of type and scrambled it to make a type specimen book. It has survived not only five centuries, but also</p>
  </article>
  <article class="card abs" style="left:416px">
    <div class="card-head"><svg class="card-icon" viewBox="0 0 104 104"><circle cx="52" cy="52" r="46" fill="#fff" stroke="#333" stroke-width="6"/><circle cx="52" cy="36" r="9" fill="#333"/><circle cx="35" cy="64" r="9" fill="#333"/><circle cx="69" cy="64" r="9" fill="#333"/><circle cx="52" cy="54" r="26" fill="none" stroke="#333" stroke-width="3"/></svg></div>
    <h2 class="card-title">COMMUNICATE</h2>
    <p class="card-text">Lorem ipsum is simply dummy text of the printing and typesetting industry. Lorem ipsum has been the industry's standard dummy text ever since the 1500s, when an unknown printer took a galley of type and scrambled it to make a type specimen book. It has survived not only five centuries, but also</p>
  </article>
  <article class="card abs" style="left:801px">
    <div class="card-head"><svg class="card-icon" viewBox="0 0 104 104"><circle cx="52" cy="52" r="46" fill="#fff" stroke="#333" stroke-width="6"/><path d="M52 26c15 0 25 10 25 22s-10 22-25 22c-4 0-7 0-10-2l-12 6 4-11c-5-4-7-9-7-15 0-12 10-22 25-22z" fill="none" stroke="#333" stroke-width="5"/><circle cx="52" cy="44" r="6" fill="#333"/><path d="M41 60c2-6 20-6 22 0" fill="#333"/></svg></div>
    <h2 class="card-title">MY LIFE</h2>
    <p class="card-text">Lorem ipsum is simply dummy text of the printing and typesetting industry. Lorem ipsum has been the industry's standard dummy text ever since the 1500s, when an unknown printer took a galley of type and scrambled it to make a type specimen book. It has survived not only five centuries, but also</p>
  </article>
</section>

<h2 class="section-title abs" style="left:90px;top:1066px">OUR <span class="o">SUCCESS</span> <span class="g">STORY</span></h2>
<ul class="success-list abs">
  <li><svg width="18" height="18" viewBox="0 0 18 18"><path d="M2 1h7l8 8-8 8H2z" fill="#fff"/></svg>More choices about your behaviours and emotions</li>
  <li><svg width="18" height="18" viewBox="0 0 18 18"><path d="M2 1h7l8 8-8 8H2z" fill="#fff"/></svg>Improve your relationships and the ways you communicate</li>
  <li><svg width="18" height="18" viewBox="0 0 18 18"><path d="M2 1h7l8 8-8 8H2z" fill="#fff"/></svg>Create better results through becoming a greater thinker</li>
  <li><svg width="18" height="18" viewBox="0 0 18 18"><path d="M2 1h7l8 8-8 8H2z" fill="#fff"/></svg>More choices about your behaviours and emotions</li>
  <li><svg width="18" height="18" viewBox="0 0 18 18"><path d="M2 1h7l8 8-8 8H2z" fill="#fff"/></svg>Improve your relationships and the ways you communicate</li>
  <li><svg width="18" height="18" viewBox="0 0 18 18"><path d="M2 1h7l8 8-8 8H2z" fill="#fff"/></svg>Create better results through becoming a greater thinker</li>
  <li><svg width="18" height="18" viewBox="0 0 18 18"><path d="M2 1h7l8 8-8 8H2z" fill="#fff"/></svg>More choices about your behaviours and emotions</li>
  <li><svg width="18" height="18" viewBox="0 0 18 18"><path d="M2 1h7l8 8-8 8H2z" fill="#fff"/></svg>Improve your relationships and the ways you communicate</li>
  <li><svg width="18" height="18" viewBox="0 0 18 18"><path d="M2 1h7l8 8-8 8H2z" fill="#fff"/></svg>Create better results through becoming a greater thinker</li>
</ul>
<h2 class="section-title abs" style="left:852px;top:1066px">WHAT <span class="o">DO YOU</span> <span class="g">DO</span></h2>
<svg class="laptop abs" viewBox="0 0 440 236">
  <rect x="52" y="0" width="336" height="216" rx="10" fill="#222" stroke="#666" stroke-width="3"/>
  <rect x="66" y="14" width="308" height="190" fill="#fff"/>
  <circle cx="220" cy="109" r="48" fill="#000"/>
  <path d="M205 86l40 23-40 23z" fill="#fff"/>
  <path d="M0 218h440l-10 14H10z" fill="#d6d6d6"/>
  <rect x="0" y="216" width="440" height="4" fill="#aaa"/>
  <rect x="190" y="218" width="60" height="4" fill="#999"/>
</svg>

<div class="rule abs" style="top:1429px"></div>

<h2 class="section-title abs" style="left:88px;top:1450px">OUR <span class="o">FEATURED</span> <span class="g">CONTENT</span></h2>
<svg class="slide-arrow abs" style="left:48px" viewBox="0 0 40 40"><circle cx="20" cy="20" r="19" fill="#fff"/><path d="M23 11l-9 9 9 9" fill="none" stroke="#000" stroke-width="4"/></svg>
<div class="feature abs" style="left:122px;background:linear-gradient(135deg,#f4d3a6,#d9764a 60%,#8a4b3a)" role="img" aria-label="Photo of a woman laughing outdoors"></div>
<div class="feature abs" style="left:365px;background:linear-gradient(180deg,#cfe7f2,#e8dcc4 55%,#9bbf74)" role="img" aria-label="Photo of a family walking on a sunny beach path"></div>
<div class="feature abs" style="left:604px;background:linear-gradient(135deg,#e9c6b4,#c58a73 60%,#f2e4dc)" role="img" aria-label="Photo of two hands holding each other"></div>
<div class="feature abs" style="left:847px;background:linear-gradient(135deg,#e65a2a,#b8734f 55%,#5a3a2c)" role="img" aria-label="Photo of a smiling group of friends"></div>
<svg class="slide-arrow abs" style="left:1106px" viewBox="0 0 40 40"><circle cx="20" cy="20" r="19" fill="#fff"/><path d="M17 11l9 9-9 9" fill="none" stroke="#000" stroke-width="4"/></svg>

<section class="team abs"></section>
<div class="avatar abs" style="left:158px" role="img" aria-label="Portrait photo of the chief executive"></div>
<p class="member-name abs" style="left:300px">Marten Hale, <span>CEO</span></p>
<p class="member-text abs" style="left:45px">Lorem ipsum is simply dummy text of the printing and typesetting industry. Lorem ipsum has been the industry's standard dummy text ever since the 1500s,</p>
<div class="avatar abs" style="left:770px" role="img" aria-label="Portrait photo of the chief executive"></div>
<p class="member-name abs" style="left:918px">Lena Corvi, <span>CEO</span></p>
<p class="member-text abs" style="left:686px">Lorem ipsum is simply dummy text of the printing and typesetting industry. Lorem ipsum has been the industry's standard dummy text ever since the 1500s,</p>
<div class="read-more abs">+ READ MORE</div>

<footer class="site-footer abs"></footer>
<div class="footer-phone abs">
  <svg width="60" height="60" viewBox="0 0 40 40"><circle cx="20" cy="20" r="18" fill="none" stroke="#fff" stroke-width="2.5"/><path d="M13 11c2-1 3 0 4 3l-1 3c1 3 3 5 6 6l3-1c3 1 4 2 3 4-2 3-5 3-9 0s-7-7-8-10 0-4 2-5z" fill="#fff"/></svg>
  CALL US: +61 02 5550 1234
</div>
<div class="follow abs">follow us:<span class="social" aria-label="Social profile"></span><span class="social" aria-label="Social profile"></span></div>
<nav class="footer-nav abs"><span>HOME</span><span>BUSINESS</span><span>INDIVIDUAL</span><span>CONTACT</span></nav>
<p class="copyright abs">COPYRIGHT@TIDES OF BLOOM</p>
<div class="footer-brand abs"><span class="brand-dot"></span><span class="brand-name">Tides Of Bloom</span></div>

</body>
</html>
```